Business card design for Velvet Harbor

We need business cards designed for our new marketing consulting company, Velvet Harbor. Our services include marketing strategy, go-to-market and launch planning, growth strategy, and execution. We serve medical technology and health technology companies, from startups to well-established growth companies.

The business cards should feel professional, credible, reliable and trustworthy, and should instill confidence. Also bold, creative, and modern.

The design must use the Velvet Harbor logo.

The primary brand color is this orange: #FF5501
A secondary color that you can use is this gray: #282B2D
I would prefer only to use the orange and gray. But if you feel you really need an additional accent color (please use it very sparingly, as little as possible), you can use this blue for small accent purposes: #009FED

Attached are the logo files. The main logo is the one with a little bit of orange on the left and the rest is gray.

The business card should include the following:

Velvet Harbor logo
First name and last name
Title
Email address
Phone number and type (in whatever order looks best for the design
Website (the website does not need to be in the same block as the personal info)

For example:

Nessa Pryle
Founder & Principal
nessa@velvetharbor.com
+1.628.309.4156 mobile (can use "." or spaces in between blocks of numbers)
velvetharbor.com (somewhere on the card, it does not need to be with the personal info; and note that there is no "www." at the beginning)

Note that there will be no address listed on the business card.

Target Market(s)

Executives (CEO, head of marketing, head of sales) at medical technology and health technology companies, mostly in their 40s and older, well-educated, often with advanced degrees. They are strategic thinkers, responsible for budgets, and familiar with P&L. Their comfort with and trust in using outside consultants varies.

Industry/Entity Type

Medical technology and health technology companies.

Contact Information for Business Card

See project description

Font styles to use
Sans Serif

Requirements
Must have
• Logo and see Business card details section above.

```html
<!DOCTYPE html>
<html lang="en">
<head>
<meta charset="utf-8">
<title>Velvet Harbor — Business Card</title>
<link rel="stylesheet" href="https://fonts.googleapis.com/css2?family=Montserrat:wght@400;500;700&display=swap">
<style>
  :root {
    --page: #1b1c1d;
    --card: #26292c;
    --orange: #e8581f;
    --white: #f2f2f2;
    --text: #e9e9e9;
  }
  * { margin: 0; padding: 0; box-sizing: border-box; }
  html, body {
    width: 1200px;
    height: 1059px;
    overflow: hidden;
    background: var(--page);
    font-family: "Montserrat", sans-serif;
  }
  .canvas { position: relative; width: 1200px; height: 1059px; }

  .card {
    position: absolute;
    background: var(--card);
    border-radius: 18px;
  }
  .card--front { left: 257px; top: 89px; width: 687px; height: 390px; }
  .card--back  { left: 254px; top: 547px; width: 693px; height: 393px; }

  .wordmark {
    font-family: "Montserrat", sans-serif;
    font-weight: 700;
    color: var(--white);
    text-transform: uppercase;
    line-height: 1.02;
  }
  .card--front .wordmark {
    position: absolute;
    left: 40px;
    top: 56px;
    font-size: 33px;
    letter-spacing: 0.16em;
  }

  .identity { position: absolute; left: 42px; top: 188px; }
  .identity__name {
    font-weight: 700;
    font-size: 26px;
    color: var(--orange);
    text-transform: uppercase;
    letter-spacing: 0.01em;
    line-height: 1.1;
  }
  .identity__title {
    font-weight: 400;
    font-size: 18px;
    color: var(--text);
    margin-top: 2px;
    letter-spacing: 0.01em;
  }

  .contacts {
    position: absolute;
    left: 41px;
    top: 263px;
    list-style: none;
  }
  .contacts__item {
    display: flex;
    align-items: center;
    height: 29.5px;
    font-size: 18px;
    font-weight: 400;
    color: var(--text);
    letter-spacing: 0.01em;
  }
  .contacts__icon { width: 14px; height: 14px; margin-right: 7px; flex: none; }

  .brand-lockup {
    position: absolute;
    inset: 0;
    display: flex;
    align-items: center;
    justify-content: center;
    gap: 26px;
  }
  .brand-lockup__dot {
    width: 22px;
    height: 22px;
    border-radius: 50%;
    background: var(--orange);
  }
  .card--back .wordmark {
    font-size: 40px;
    letter-spacing: 0.17em;
  }
</style>
</head>
<body>
<main class="canvas">

  <section class="card card--front" aria-label="Business card front">
    <div class="wordmark">Velvet<br>Harbor</div>

    <div class="identity">
      <p class="identity__name">Nessa Pryle</p>
      <p class="identity__title">Founder &amp; Principal</p>
    </div>

    <ul class="contacts">
      <li class="contacts__item">
        <svg class="contacts__icon" viewBox="0 0 16 16" aria-hidden="true">
          <path fill="#e8581f" d="M2 5c0-2 2.5-3 6-3s6 1 6 3v1.5h-3.5V5h-5v1.5H2zM4 8l2-2h4l2 2 1.5 5.5h-11z"/>
          <circle cx="8" cy="10.5" r="1.6" fill="#26292c"/>
        </svg>
        +1.628.309.4156
      </li>
      <li class="contacts__item">
        <svg class="contacts__icon" viewBox="0 0 16 16" aria-hidden="true">
          <path fill="#e8581f" d="M1 6l7-5 7 5v9H1z"/>
          <path fill="none" stroke="#26292c" stroke-width="1.3" d="M1.5 6.5l6.5 5 6.5-5M1.5 14.5l4.5-4M14.5 14.5l-4.5-4"/>
        </svg>
        nessa@velvetharbor.com
      </li>
      <li class="contacts__item">
        <svg class="contacts__icon" viewBox="0 0 16 16" aria-hidden="true">
          <circle cx="8" cy="8" r="7" fill="#e8581f"/>
          <path fill="#26292c" d="M5 3.5c1.5 0 2.5 1 2 2.5S5 7 5.5 8.5 4 10 3 8.5 3 4 5 3.5zM9.5 9c1.5-.5 3 .5 2.5 2s-2 2.5-3 1.5.5-1.5.5-3.5z"/>
        </svg>
        velvetharbor.com
      </li>
    </ul>
  </section>

  <section class="card card--back" aria-label="Business card back">
    <div class="brand-lockup">
      <span class="brand-lockup__dot" aria-hidden="true"></span>
      <div class="wordmark">Velvet<br>Harbor</div>
    </div>
  </section>

</main>
</body>
</html>
```